Internal Company (Private/Invite only) blog

I need a template for an internal company blog.
We are an FMCG organisation operating in Saudi Arabia. We have large number of partners working with us across multiple countries.
This blog is primarily designed to inform our shareholders of progress/updates, new information etc.
It will be published/updated weekly

Target Market(s)

audience is company stakeholders only

Industry/Entity Type

It Company

Requirements
Must have
• - Core feature must be that this can be secure/private as we wish to submit information that is only for a registered list of readers.

- ability to update content with images and content
Nice to have
• Some elements we have thought of
- Contact details
- Personnel Bio's
- Weekly product review
- Status on activities
- Case studies
- Future discussion points
- Glossary of terms
- submit your question/idea

Also would like to have ability to have published posts sent to the readers either as a link or as an email with the new content in the message body of the email
Should not have
• No complicated interface.
Should be easy, clean and simple layout
No business type imagery such as pie charts, graphs etc

```html
<!DOCTYPE html>
<html lang="en">
<head>
<meta charset="utf-8">
<title>Internal Blog</title>
<link rel="stylesheet" href="https://fonts.googleapis.com/css2?family=Arimo:wght@400;700&family=Ubuntu:wght@400&display=swap">
<style>
:root{
  --ink:#2b2b2b;
  --muted:#8a8a8a;
  --link:#0a4d8c;
  --link-soft:#1e7fc4;
  --rule:#9a9a9a;
  --panel-top:#5eacf6;
  --panel-bottom:#0b5ca6;
  --panel-edge:#2c79c6;
  --panel-text:#ffffff;
  --footer-band:#dcecfb;
}
*{box-sizing:border-box;margin:0;padding:0}
html,body{width:1125px;height:1200px;overflow:hidden;background:#fff}
.page{position:relative;width:1190px;height:1270px;transform:scale(0.9454);transform-origin:0 0;font-family:Arimo,Arial,sans-serif;color:var(--ink)}
.abs{position:absolute}
.rule{position:absolute;left:96px;width:691px;border-top:1px dashed var(--rule)}
.meta{font-size:10px;color:var(--muted);letter-spacing:.2px}
.meta a{color:var(--link);font-weight:700;text-decoration:underline}
.meta .sep{margin:0 4px;color:var(--muted)}
.share{display:flex;gap:4px;align-items:center}
.share .btn{height:19px;border:1px solid #cfcfcf;border-radius:2px;background:linear-gradient(#fff,#eee);font-size:11px;color:#777;display:flex;align-items:center;padding:0 6px;gap:5px}
.share .dot{width:10px;height:10px;border-radius:50%;background:#7cb87a}
.share .sq{width:10px;height:10px;background:#8cc3ea}
.share .sq.dark{background:#3b5b99}
.share .count{width:20px;height:17px;border:1px solid #bbb;font-size:10px;display:flex;align-items:center;justify-content:center;color:#333;background:#fff}
.body-text{font-size:12px;line-height:18px;color:var(--ink);letter-spacing:.1px}
.body-text p+p{margin-top:18px}
.more{font-size:11px;color:var(--link-soft);text-decoration:underline}
.post-title{font-size:18px;color:#222;font-weight:400}
.media{border:1px solid #bdbdbd;padding:3px;background:#fff}
.media .fill{width:100%;height:100%}
.panel{position:absolute;left:807px;width:306px;border-radius:9px;border:1px solid var(--panel-edge);background:linear-gradient(var(--panel-top),var(--panel-bottom));color:var(--panel-text)}
.panel h2{font-family:Arimo,Arial,sans-serif;font-weight:400;font-size:18px;margin:12px 0 0 13px}
.panel hr{border:0;border-top:1px solid rgba(255,255,255,.45);margin:8px 14px 0 13px}
.panel ul{list-style:none;margin:17px 18px 0 12px}
.panel li{display:flex;font-family:Ubuntu,Tahoma,sans-serif;font-size:10.5px;line-height:13px;margin-bottom:7px}
.panel li::before{content:"»";width:20px;flex:none;font-size:13px;line-height:12px}
.panel a{color:var(--panel-text);text-decoration:underline}
.tags{margin:11px 14px 0 20px;font-family:Ubuntu,Tahoma,sans-serif;font-size:10.5px;line-height:20px}
.tags a{margin-right:5px}
.tags .lg{font-size:13.5px}
.footer-band{position:absolute;left:90px;top:1136px;width:1025px;height:80px;background:linear-gradient(var(--footer-band),rgba(255,255,255,0) 90%)}
.footer-band::before{content:"";position:absolute;left:0;right:0;top:0;height:2px;background:linear-gradient(90deg,rgba(80,140,200,0),#5e8fc0 30%,#5e8fc0 70%,rgba(80,140,200,0))}
.footer-nav{font-size:11px;color:#222}
.footer-nav span.sep{margin:0 10px}
.copy{font-size:11px;color:#222}
.subscribe h3{font-size:14px;font-weight:400;color:#111}
.subscribe .field{margin-top:6px;width:251px;height:25px;border:1px solid #aaa;border-radius:4px;background:#fff;display:flex;align-items:center;justify-content:space-between;padding:0 4px 0 6px;font-size:12px;color:#aaa}
</style>
</head>
<body>
<div class="page">

  <main>
    <div class="rule" style="top:9px"></div>
    <article>
      <div class="meta abs" style="left:98px;top:22px">Posted at 11:55 PM in <a>Lane Morrow</a>, <a>Podcasts</a><span class="sep">|</span><a>Permalink</a><span class="sep">|</span><a>Comments (0)</a></div>
      <div class="share abs" style="left:98px;top:38px">
        <span class="btn"><span class="dot"></span>Share (0)</span>
        <span class="btn"><span class="sq"></span>Post This!</span>
        <span class="btn"><span class="sq dark"></span>Like</span>
        <span class="count">2</span>
        <svg width="22" height="14" viewBox="0 0 22 14"><rect x="1" y="1" width="20" height="12" fill="#f7d35a" stroke="#d9a21d"/><path d="M1 1l10 7 10-7" fill="none" stroke="#d9a21d"/></svg>
      </div>
      <div class="media abs" style="left:512px;top:56px;width:275px;height:394px">
        <div class="fill" role="img" aria-label="Stack of coloured letter cubes spelling a word" style="background:linear-gradient(160deg,#f4f4f4,#e4e4e4)"></div>
      </div>
      <div class="body-text abs" style="left:99px;top:79px;width:392px">
        <p>LMT is the creator, co-founder and host of the Open Table podcast, the edgiest show on Tactica: the Card Game available online. Even with the success of this podcast, he has always wanted to do something that was safe for work and here it is, an interview with the only Canadian player inducted in the Hall of Fame, Dale Ferris. Dale has included some excellent advice not only for players of the game, but writers as well.</p>
        <p>LMT is the creator, co-founder and host of the Open Table podcast, the edgiest show on Tactica: the Card Game available online. Even with the success of this podcast, he has always wanted to do something that was safe for work and here it is, an interview with the only Canadian player inducted in the Hall of Fame, Dale Ferris. Dale has included some excellent advice not only for players of the game, but writers as well.LMT is the creator, co-founder and host of the Open Table podcast, the edgiest show on Tactica: the Card Game available online. Even with the success of this podcast, he has always wanted to do something that was safe for work and here it is, an interview with the only Canadian player inducted in the Hall of Fame, Dale Ferris. Dale has included some excellent advice not only for players of the game, but writers as well.</p>
      </div>
      <div class="body-text abs" style="left:99px;top:467px;width:686px">
        <p>LMT is the creator, co-founder and host of the Open Table podcast, the edgiest show on Tactica: the Card Game available online. Even with the success of this podcast, he has always wanted to do something that was safe for work and here it is, an interview with the only Canadian player inducted in the Hall of Fame, Dale Ferris. Dale has included some excellent advice not only for players of the game, but writers as well.</p>
        <p>LMT is the creator, co-founder and host of the Open Table podcast, the edgiest show on Tactica: the Card Game available online. Even with the success of this podcast, he has always wanted to do something that was safe for work and here it is, an interview with the only Canadian player inducted in the Hall of Fame, Dale Ferris.</p>
      </div>
      <a class="more abs" style="left:99px;top:628px">Continue Reading</a>
    </article>

    <article>
      <h1 class="post-title abs" style="left:97px;top:663px">Lorel IPsum Dolor sit amet</h1>
      <div class="rule" style="top:691px"></div>
      <div class="meta abs" style="left:98px;top:705px">Posted at 11:55 PM in <a>Lane Morrow</a>, <a>Podcasts</a><span class="sep">|</span><a>Permalink</a><span class="sep">|</span><a>Comments (0)</a></div>
      <div class="share abs" style="left:98px;top:721px">
        <span class="btn"><span class="dot"></span>Share (0)</span>
        <span class="btn"><span class="sq"></span>Post This!</span>
        <span class="btn"><span class="sq dark"></span>Like</span>
        <span class="count">2</span>
        <svg width="22" height="14" viewBox="0 0 22 14"><rect x="1" y="1" width="20" height="12" fill="#f7d35a" stroke="#d9a21d"/><path d="M1 1l10 7 10-7" fill="none" stroke="#d9a21d"/></svg>
      </div>
      <div class="media abs" style="left:500px;top:739px;width:287px;height:314px;padding:2px">
        <div class="fill" role="img" aria-label="Green figure pushing a shopping cart among red discount cubes" style="background:radial-gradient(circle at 60% 55%,#e9f3e2 0,#fff 60%),#fff;background-color:#fbeeee"></div>
      </div>
      <div class="body-text abs" style="left:99px;top:762px;width:392px">
        <p>LMT is the creator, co-founder and host of the Open Table podcast, the edgiest show on Tactica: the Card Game available online. Even with the success of this podcast, he has always wanted to do something that was safe for work and here it is, an interview with the only Canadian player inducted in the Hall of Fame, Dale Ferris. Dale has included some excellent advice not only for players of the game, but writers as well.</p>
        <p>LMT is the creator, co-founder and host of the Open Table podcast, the edgiest show on Tactica: the Card Game available online. Even with the success of this podcast, he has always wanted to do something that was safe for work and here it is, an interview with the only Canadian player inducted in the Hall of Fame, Dale Ferris. Dale has included some excellent advice not only for players of the game, but writers as well.</p>
      </div>
      <a class="more abs" style="left:100px;top:1045px">Continue Reading</a>
    </article>
  </main>

  <aside>
    <section class="panel" style="top:14px;height:276px">
      <h2>Recent Comments</h2><hr>
      <ul>
        <li><a>&nbsp;Riverjd on Why UG Wave beats Ux control</a></li>
        <li><a>&nbsp;Evan on Why UG Wave beats Ux control</a></li>
        <li><a>Riverjd on Why UG Wave beats Ux control</a></li>
        <li><a>TheTeacher_K on My Path to the Pro Tour Circuit and Worlds *37th* Place</a></li>
        <li><a>Owen on Why UG Wave beats Ux control</a></li>
        <li><a>Riverjd on Why UG Wave beats Ux control</a></li>
        <li><a>Ivy (PaperSage) on Why UG Wave beats Ux control&nbsp;</a></li>
      </ul>
    </section>

    <section class="panel" style="top:300px;height:188px">
      <h2>Categories</h2><hr>
      <div class="tags">
        <a>Alan Tessler</a> <a>Alex Brandt</a> <a>Broken City Cards</a>
        <a>Clara Vance</a> <a>Dean Kolb</a> <a>Deck Tech</a> <a class="lg">Doug Palmer</a> <a class="lg">EDH</a>
        <a>Extended</a> <a>Felix Tremblay</a> <a>Fabien Roux</a>
        <a>French General</a> <a>Ivan Baird</a> <a>Interview</a>
        <a class="lg">Jordan Smythe</a> <a>Judge</a> <a>Julian Richter</a>
        <a class="lg">Lane Morrow</a> <a>Kenta Tamura</a> <a>Legacy</a>
      </div>
    </section>

    <section class="panel" style="top:497px;height:276px">
      <h2>Archieves</h2><hr>
      <ul style="margin-top:19px">
        <li><a>June 2011</a></li>
        <li><a>July 2011</a></li>
        <li><a>August 2011</a></li>
        <li><a>September 2011</a></li>
        <li><a>Decemeber 2011</a></li>
        <li><a>January 2012</a></li>
        <li><a>March 2012</a></li>
        <li><a>April 2012</a></li>
        <li><a>May 2012</a></li>
      </ul>
    </section>
  </aside>

  <footer>
    <div class="footer-band"></div>
    <nav class="footer-nav abs" style="left:113px;top:1166px">Home<span class="sep">|</span>Bios<span class="sep">|</span>Product Review<span class="sep">|</span>Activities<span class="sep">|</span>Case Studies<span class="sep">|</span>Discussion<span class="sep">|</span>Glossary<span class="sep">|</span>FAQ<span class="sep">|</span>Contact</nav>
    <div class="copy abs" style="left:113px;top:1187px">© 2012, All Rights Reserved</div>
    <div class="subscribe abs" style="left:833px;top:1154px">
      <h3>Subscribe Newsletter</h3>
      <div class="field">Type your email id
        <svg width="16" height="16" viewBox="0 0 16 16"><rect x="1.5" y="2.5" width="12" height="12" rx="2" fill="none" stroke="#222" stroke-width="1.6"/><path d="M4 8l3 3 7-9" fill="none" stroke="#222" stroke-width="2"/></svg>
      </div>
    </div>
  </footer>

</div>
</body>
</html>
```